依頼詳細
現在、お店のロゴはあります。既存のロゴを使用して、立て看板を新しくしたいと思っています。看板の入稿に必要なデザインをillustratorで作成して頂きたいと思います。
重視するポイントは、
1。概要、特徴にも記載しましたが2Fとわかること。
2.ワインはそうですが、お食事ができること。
3.現在使用しているロゴを看板の中心にもっていってワインと一目でわかるようにしたい
4.現在の立て看板がとてもカジュアルな為、店内の雰囲気とかなりギャップがあります。若年の方が立ち飲みバルや、居酒屋、カフェ等と間違えて誤って入ってこられることがたまにあります。お店の雰囲気がでるようなシンプルで雰囲気のあるデザインを希望します。看板製作会社が、完全データの支給を要求しているため、Adobe Illustratorアウトラインデータ Mac=8.0 Win=CSにて納品お願いします。
お店の雰囲気、現在の看板、ロゴなどは添付ファイル参照ください。
記載項目
店舗名、2F、ワインとお食事、今のロゴ。定番メニューのリスト、電話番号。席数。
希望イメージ
シンプル 複雑
単色 カラフル
暗い 明るい
日常 高級
遊び心 厳粛
未来的 伝統的
女性的 男性的
希望する色
白、ワインレッド系、ロゴに合わせたカラー
納品ファイル
• 高解像度JPG (.jpg)
• イラストレーター形式 (.ai)
補足説明
入口の間口が狭いために、看板に必ず2F+↑を記載していただきたいです。表、左上がり、裏、右上がりの☝をつけてほしいです。現在の立て看板ファイルを参照してください。
看板仕上がりサイズはW600×H900です。【画面有効サイズ】 W530×H830mmとなっています。内側に投光機を設置し、ライトアップされます。宜しくお願いいたします。
■ 選んだ理由

現在の問題点をクリアし、お店の雰囲気が看板一つで出ている所。

■ 提案者全員のお礼・コメント

修正等にご対応いただきまして誠にありがとうございました。今後も名刺の修正等依頼していくつもりですので機会がありましたら是非とも宜しくお願いいたします。

```html
<!DOCTYPE html>
<html lang="ja">
<head>
<meta charset="utf-8">
<title>VERANO – Wine &amp; Dine Stand Sign</title>
<link rel="stylesheet" href="https://fonts.googleapis.com/css2?family=Noto+Sans+JP:wght@400;500;700&family=Shippori+Mincho:wght@500;600&family=Cormorant+Garamond:wght@500&display=swap">
<style>
  :root {
    --frame: #6e6c6a;
    --panel: #d8d1c7;
    --ink: #2b2420;
    --wine: #9b1b2a;
    --plate: #ffffff;
    --plate-ring: #8a8784;
  }
  html, body {
    margin: 0;
    padding: 0;
    width: 799px;
    height: 1200px;
    overflow: hidden;
    background: var(--frame);
  }
  .sign {
    display: block;
    width: 799px;
    height: 1200px;
  }
  .sign__frame { fill: var(--frame); }
  .sign__panel { fill: var(--panel); }
  .floor-guide__line {
    fill: none;
    stroke: var(--ink);
    stroke-width: 5;
    stroke-linejoin: miter;
  }
  .floor-guide__arrow {
    fill: none;
    stroke: var(--ink);
    stroke-width: 5;
  }
  .floor-guide__label {
    font-family: "Cormorant Garamond", "Shippori Mincho", serif;
    font-size: 74px;
    font-weight: 500;
    fill: var(--ink);
  }
  .seating {
    font-family: "Noto Sans JP", sans-serif;
    font-size: 38px;
    font-weight: 400;
    fill: var(--ink);
  }
  .brand__dot { fill: var(--wine); }
  .brand__tagline {
    font-family: "Noto Sans JP", sans-serif;
    font-size: 34px;
    font-weight: 500;
    letter-spacing: 1px;
    fill: var(--ink);
  }
  .brand__name {
    font-family: "Noto Sans JP", sans-serif;
    font-size: 116px;
    font-weight: 500;
    letter-spacing: 4px;
    fill: var(--ink);
  }
  .brand__phone {
    font-family: "Noto Sans JP", sans-serif;
    font-size: 42px;
    font-weight: 500;
    fill: var(--ink);
  }
  .plate__ring { fill: var(--plate-ring); }
  .plate__face { fill: var(--plate); stroke: var(--ink); stroke-width: 2; }
  .plate__headline {
    font-family: "Shippori Mincho", serif;
    font-size: 84px;
    font-weight: 500;
    letter-spacing: 8px;
    fill: var(--ink);
  }
  .menu__item {
    font-family: "Shippori Mincho", serif;
    font-size: 33px;
    font-weight: 500;
    fill: var(--ink);
  }
</style>
</head>
<body>
<svg class="sign" viewBox="0 0 799 1200" xmlns="http://www.w3.org/2000/svg" role="img" aria-label="VERANO wine and dine second floor stand sign">
  <defs>
    <clipPath id="panel-clip">
      <rect x="27" y="27" width="745" height="1146"/>
    </clipPath>
    <path id="headline-arc" d="M 40 900 A 636 636 0 0 1 760 900"/>
  </defs>

  <rect class="sign__frame" x="0" y="0" width="799" height="1200"/>
  <rect class="sign__panel" x="27" y="27" width="745" height="1146"/>

  <g class="floor-guide">
    <path class="floor-guide__line" d="M105 92 V198 H355 V342 H772"/>
    <path class="floor-guide__arrow" d="M200 165 L150 115 M150 115 H178 M150 115 V143"/>
    <text class="floor-guide__label" x="252" y="190">2F</text>
  </g>

  <g class="seating">
    <text x="386" y="264">テーブル　10席</text>
    <text x="386" y="312">カウンター 7席</text>
  </g>

  <g class="brand">
    <circle class="brand__dot" cx="160" cy="510" r="58"/>
    <text class="brand__tagline" x="400" y="458">WINE &amp; DINE</text>
    <text class="brand__name" x="250" y="565">VERANO</text>
    <text class="brand__phone" x="372" y="625">090-4827-3561</text>
  </g>

  <g class="plate" clip-path="url(#panel-clip)">
    <circle class="plate__ring" cx="400" cy="1171" r="534"/>
    <circle class="plate__face" cx="400" cy="1171" r="520"/>
    <text class="plate__headline">
      <textPath href="#headline-arc" startOffset="50%" text-anchor="middle">ワインとお食事</textPath>
    </text>
    <g class="menu" text-anchor="middle">
      <text class="menu__item" x="400" y="884">国産牛トリッパの煮込</text>
      <text class="menu__item" x="400" y="942">自家製レバーパテ</text>
      <text class="menu__item" x="400" y="1000">季節のお魚のカルパッチョ</text>
      <text class="menu__item" x="400" y="1058">季節の食材を使用したパスタ２種</text>
      <text class="menu__item" x="400" y="1112">…　etc　…</text>
    </g>
  </g>
</svg>
</body>
</html>
```